Vehicle and Trailer Signage, Vehicle Wrap, Need a concept URGENTLY

We need a moving billboard.
Our business vehicle and trailer needs to stand out. We have multiple services we offer and need a corporate image and rolling billboard/advertisement that represents us.

We start from cleaning carpet and tiles, to upholstery and curtians, to completely clean all contents and building materials after a fire, or completely dry out a home or business after a major or minor flood event. We are open to all concepts as we want to create a modern new professional look.

Use our current logo, or modify to suite. Use our website www.brightvaleworks.com.au for current logo and all other past ideas.
The vehicle is a Marlowe Ridge rover 300 series with major modification and a 7 metre trailer. The Ridge rover is Silver. The trailer can be white or silver as it has not yet been painted.

The Vehicle is used for cleaning carpet and tiles, upholstery and curtains, etc The Trailer is used for cleaning all contents and building materials after a fire, or carrying the equipment to completely dry out a home or business after a major or minor flood event.

I would like to see the sides of the vehicle and trailer completed first, then we can move on to the fronts and backs as it will flow better that way.

We will need to follow up with uniforms and letterheads and would like the winning designer to be part of that, etc.

Project Deadline Extended Reason: I need more quality designs to see, more ideas to buzz in my head Added Tuesday, October 21, 2014

Project Deadline Extended Reason: Still have not received a completed design, This will be guaranteed payment if i receive a completed design. Added Sunday, October 26, 2014

Target Market(s)

Our target market is everyone. Home owners to business managers. Employees to rental tenants. We aim at the more upmarket client, but we provide our services to everyone in between.

Industry/Entity Type

Business

Font styles to use
Sans Serif

Colors
e34197
0692cd
f37123
fbed23
ffc213
0255a3
33a6d7
9bcb3c

Requirements
Must have
• Must attract attention - Think Moving Billboard
• This is our moving business card - It needs to say what we do and stamp it in their mind.
Nice to have
• I like the fire and water colour and graphics on the race car, one side orange and yellow (fire) and the other side, blues (water). As we do fire and water damage work.
• BUT THIS IS NOT NECESSARY.
• The Blue along each side works great - as long as i dont get taken as a pool cleaner any more.....
Should not have
• Please do not submit a plain design as it will be a waste of our time unless significant effort has been put in.
• I will add more participation payments if i think that they are on track and meet the brief. Please help me finish this design quickly.

```html
<!DOCTYPE html>
<html lang="en">
<head>
<meta charset="utf-8">
<title>Brightvale Works – Vehicle Side Panels</title>
<link rel="stylesheet" href="https://fonts.googleapis.com/css2?family=Open+Sans:wght@600&family=Permanent+Marker&display=swap">
<style>
  :root {
    --paper: #ffffff;
    --navy: #163a7a;
    --royal: #0d4a9e;
    --pink: #e0157a;
    --sky: #33a6d7;
    --sky-bright: #1fa3ee;
    --fire-core: #fff1c4;
    --fire-mid: #f37123;
    --fire-deep: #7a1a08;
    --water-light: #3fb6f2;
    --water-deep: #0a2f8c;
    --halo: #f7e9c8;
  }
  html, body {
    margin: 0;
    padding: 0;
    width: 848px;
    height: 1200px;
    overflow: hidden;
    background: var(--paper);
  }
  .wrap-sheet {
    display: block;
    width: 848px;
    height: 1200px;
  }
  .brand-name {
    font-family: "Open Sans", Arial, Helvetica, sans-serif;
    font-weight: 600;
    font-size: 42px;
    fill: var(--paper);
  }
  .tagline {
    font-family: "Permanent Marker", "Arial Black", Arial, sans-serif;
    font-size: 50px;
    fill: var(--paper);
  }
</style>
</head>
<body>
<svg class="wrap-sheet" viewBox="0 0 848 1200" xmlns="http://www.w3.org/2000/svg">
  <defs>
    <radialGradient id="fireGlow" cx="0.6" cy="0.55" r="0.7">
      <stop offset="0" stop-color="var(--fire-core)"/>
      <stop offset="0.35" stop-color="var(--fire-mid)"/>
      <stop offset="0.8" stop-color="var(--fire-deep)"/>
      <stop offset="1" stop-color="#2a1240"/>
    </radialGradient>
    <radialGradient id="waterGlow" cx="0.45" cy="0.6" r="0.75">
      <stop offset="0" stop-color="var(--water-light)"/>
      <stop offset="0.6" stop-color="#1565d0"/>
      <stop offset="1" stop-color="var(--water-deep)"/>
    </radialGradient>
  </defs>

  <!-- Fire side panel -->
  <g class="panel panel-fire">
    <rect class="panel-art" x="26" y="57" width="806" height="358" fill="url(#fireGlow)"
          role="img" aria-label="Photographic fire and flames background"/>
    <g class="accent-stripes" fill="var(--pink)">
      <polygon points="290,72 832,58 832,128 700,118 520,98"/>
      <polygon points="560,130 832,150 832,330 720,330 700,250"/>
      <polygon points="110,322 380,398 300,415 180,415"/>
      <polygon points="300,345 470,410 400,415"/>
    </g>
    <polygon class="brand-band" points="26,100 440,190 440,370 26,290" fill="var(--royal)" stroke="var(--pink)" stroke-width="6"/>
    <circle class="brand-disc" cx="470" cy="300" r="95" fill="var(--halo)" stroke="var(--pink)" stroke-width="9"/>
    <text class="brand-name" transform="translate(40,200) rotate(13)" textLength="315" lengthAdjust="spacingAndGlyphs">Brightvale Works</text>
    <path class="tag-band" d="M26,415 H832 V505 L555,525 A68,30 0 0 0 420,525 A65,30 0 0 0 290,525 L26,520 Z" fill="var(--navy)"/>
    <text class="tagline" x="48" y="482" textLength="765" lengthAdjust="spacingAndGlyphs">WE DON'T CUT CORNERS</text>
  </g>

  <!-- Water side panel -->
  <g class="panel panel-water">
    <rect class="panel-art" x="26" y="609" width="806" height="356" fill="url(#waterGlow)"
          role="img" aria-label="Photographic water droplets background"/>
    <g class="accent-stripes" fill="var(--sky-bright)">
      <polygon points="26,640 560,625 300,670 70,690"/>
      <polygon points="26,700 250,690 160,760 26,790"/>
      <polygon points="26,860 220,880 26,930"/>
      <polygon points="560,935 760,870 832,870 832,965 620,965"/>
    </g>
    <polygon class="brand-band" points="430,770 832,660 832,800 430,930" fill="var(--royal)" stroke="var(--sky)" stroke-width="5"/>
    <circle class="brand-disc" cx="375" cy="840" r="120" fill="var(--sky)" stroke="var(--royal)" stroke-width="12"/>
    <text class="brand-name" transform="translate(505,835) rotate(-13)" textLength="295" lengthAdjust="spacingAndGlyphs">Brightvale Works</text>
    <path class="tag-band" d="M26,965 H832 V1075 L575,1085 A68,30 0 0 0 440,1085 A65,30 0 0 0 310,1085 L26,1085 Z" fill="var(--navy)"/>
    <text class="tagline" x="150" y="1040" textLength="520" lengthAdjust="spacingAndGlyphs">WE CLEAN THEM</text>
  </g>
</svg>
</body>
</html>
```